Wendale Ridge Concrete Pumping needs a logo design and is in the concrete industry

A creative design for this Wendale Ridge Concrete Pumping business. Using a trailer mounted line pump, not a boom pump.
Colour to be used is orange and a mix of white or black writing.
Target Market(s)
General Public, anyone
Industry/Entity Type
Concrete
Contact Information for Business Card
Wendale Ridge Concrete Pumping
Callum Hesketh
PO BOX 47
Colac VIC 3250
Phone: 0417952803
Email: Hesketh@bluewrenmail.com.au
Colors
f37122
000000
ffffff
Requirements
Must have
- Details listed
Nice to have
- A great logo
Should not have
- anything silly

```html
<!DOCTYPE html>
<html lang="en">
<head>
<meta charset="utf-8">
<title>Wendale Ridge Concrete Pumping – Business Card</title>
<link href="https://fonts.googleapis.com/css2?family=Open+Sans:wght@400;600&family=Roboto:wght@500&display=swap" rel="stylesheet">
<style>
  :root {
    --orange: #f37122;
    --orange-deep: #ee6a1c;
    --orange-light: #f47c31;
    --card-white: #f3f3f3;
    --ink: #222222;
    --stage: #000000;
    --white: #ffffff;
  }
  * { margin: 0; padding: 0; box-sizing: border-box; }
  html, body {
    width: 1200px; height: 900px; overflow: hidden;
    background: var(--stage);
  }
  .canvas { position: relative; width: 1200px; height: 900px; }

  .card {
    position: absolute; top: 200px; width: 310px; height: 502px; overflow: hidden;
  }
  .card-front {
    left: 265px; background: var(--card-white);
    border-radius: 62px 0 62px 0;
  }
  .card-back {
    left: 641px;
    border-radius: 0 62px 0 62px;
  }

  .brand {
    position: absolute; top: 40px; left: 0; right: 0;
    display: flex; flex-direction: column; align-items: center;
    color: var(--orange);
  }
  .brand-mark {
    width: 58px; height: 58px; background: var(--orange); margin-bottom: 16px;
  }
  .brand-name {
    font-family: "Roboto", sans-serif; font-weight: 500;
    font-size: 35px; line-height: 1; letter-spacing: -0.3px;
  }
  .brand-tagline {
    font-family: "Roboto", sans-serif; font-weight: 500;
    font-size: 14px; letter-spacing: 4.2px; margin-top: 8px;
  }

  .contact {
    position: absolute; left: 27px; top: 327px;
    font-family: "Open Sans", sans-serif; color: var(--ink);
  }
  .contact-name {
    font-weight: 600; font-size: 18px; color: var(--orange); letter-spacing: 0.2px;
  }
  .contact-role { font-size: 14px; margin-top: 4px; }
  .contact-address { font-size: 13.5px; line-height: 16px; margin-top: 18px; }
  .contact-lines { list-style: none; margin-top: 10px; font-size: 13.5px; }
  .contact-lines li { display: flex; align-items: center; gap: 7px; height: 19px; }
  .contact-lines svg { width: 10px; height: 10px; fill: var(--orange); }

  .back-field {
    position: absolute; inset: 0;
    background: linear-gradient(180deg, var(--orange-light) 0%, var(--orange-deep) 55%, var(--orange-light) 100%);
  }
  .back-brand {
    position: absolute; left: 0; right: 0; top: 372px;
    text-align: center; color: var(--white);
  }
  .back-brand .brand-name { font-size: 33px; }
  .back-brand .brand-tagline { font-size: 14px; margin-top: 9px; }
</style>
</head>
<body>
<main class="canvas">

  <section class="card card-front" aria-label="Business card front">
    <header class="brand">
      <div class="brand-mark" aria-hidden="true"></div>
      <div class="brand-name">Wendale Ridge</div>
      <div class="brand-tagline">CONCRETE PUMPING</div>
    </header>

    <div class="contact">
      <p class="contact-name">JOHN SMITH</p>
      <p class="contact-role">Managing Director</p>
      <p class="contact-address">1234, Address Goes Here<br>Country Name, 123456</p>
      <ul class="contact-lines">
        <li>
          <svg viewBox="0 0 10 10" aria-hidden="true"><path d="M1 3.2C1 2 2.5 1.5 5 1.5S9 2 9 3.2V4H7V3H3v1H1z M2 5h6l1 3.5H1z"/></svg>
          823-456-7890
        </li>
        <li>
          <svg viewBox="0 0 10 10" aria-hidden="true"><path d="M0.5 2h9v6h-9z" /><path d="M0.8 2.3L5 5.6l4.2-3.3" stroke="#f3f3f3" stroke-width="0.9" fill="none"/></svg>
          info@youremail.com
        </li>
      </ul>
    </div>
  </section>

  <section class="card card-back" aria-label="Business card back">
    <div class="back-field" role="img" aria-label="Orange field with a faint large brand decoration"></div>
    <div class="back-brand">
      <div class="brand-name">Wendale Ridge</div>
      <div class="brand-tagline">CONCRETE PUMPING</div>
    </div>
  </section>

</main>
</body>
</html>
```